Business Cards for a law firm

Business cards for our law firm. Use our silhoette logo and OAK HARBOR - check our website (www.oakharbor-legal.com)

Contact Information for Business Card

our silhouette logo, OAK HARBOR, 800-555-0147, Dorian Kestrup, dorian@oakharbor-legal.com

Requirements
Must have
• our silhouette logo, OAK HARBOR, 800-555-0147, Dorian Kestrup, dorian@oakharbor-legal.com

```html
<!DOCTYPE html>
<html lang="en">
<head>
<meta charset="utf-8">
<title>Oak Harbor – Business Cards</title>
<link rel="stylesheet" href="https://fonts.googleapis.com/css2?family=Cinzel:wght@700&family=Crimson+Text&family=Arimo:ital@1&display=swap">
<style>
  :root {
    --stage: #fdc113;
    --front-bg: #68661c;
    --front-rule: #524f0a;
    --front-mark: #555006;
    --front-ink: #ffffff;
    --back-bg: #e3ca55;
    --back-band: #857230;
    --back-mark: #b49c42;
    --back-ink: #7a6417;
    --shadow: rgba(70, 45, 0, 0.55);
  }
  * { box-sizing: border-box; margin: 0; padding: 0; }
  html, body {
    width: 1200px; height: 1200px; overflow: hidden;
    background: var(--stage);
  }
  .card {
    position: absolute; left: 220px; width: 772px; height: 441px;
    box-shadow: 6px 8px 8px var(--shadow);
    overflow: hidden;
  }
  .card--front { top: 100px; background: var(--front-bg); }
  .card--back  { top: 594px; background: var(--back-bg); }

  .front-frame {
    position: absolute; left: 16px; top: 17px; right: 16px; bottom: 17px;
    border: 3px solid var(--front-rule);
  }
  .front-mark {
    position: absolute; left: 280px; top: 58px; width: 211px; height: 323px;
    background: var(--front-mark); border-radius: 40px 40px 6px 6px;
  }
  .firm-name {
    position: absolute; left: 0; right: 0; top: 148px;
    text-align: center; color: var(--front-ink);
    font-family: "Cinzel", serif; font-weight: 700;
    font-size: 58px; letter-spacing: 4px; line-height: 1;
  }
  .firm-tagline {
    position: absolute; left: 0; right: 0; top: 226px;
    text-align: center; color: var(--front-ink);
    font-family: "Crimson Text", serif; font-size: 33px; line-height: 1;
  }
  .front-url {
    position: absolute; left: 0; right: 0; top: 388px;
    text-align: center; color: var(--front-ink);
    font-family: "Arimo", sans-serif; font-style: italic; font-size: 18px;
  }

  .back-mark {
    position: absolute; left: 41px; top: 72px; width: 205px; height: 309px;
    background: var(--back-mark); border-radius: 40px 40px 6px 6px;
  }
  .back-band {
    position: absolute; left: 0; right: 0; bottom: 0; height: 26px;
    background: var(--back-band);
  }
  .contact {
    position: absolute; left: 410px; top: 108px;
    color: var(--back-ink);
    font-family: "Arimo", sans-serif; font-style: italic;
  }
  .contact-name { font-size: 41px; line-height: 1; }
  .contact-role { font-size: 22px; margin-top: 8px; line-height: 1; }
  .contact-list { list-style: none; margin-top: 54px; }
  .contact-item {
    display: flex; align-items: center; gap: 12px;
    font-size: 19px; height: 26px; margin-bottom: 19px;
  }
  .contact-icon { width: 28px; height: 28px; flex: none; fill: var(--back-ink); }
</style>
</head>
<body>
  <section class="card card--front" aria-label="Card front">
    <div class="front-frame"></div>
    <div class="front-mark" role="img" aria-label="Firm silhouette logo: two standing men in suits"></div>
    <h1 class="firm-name">OAK HARBOR</h1>
    <p class="firm-tagline">Law Firm</p>
    <p class="front-url">www.oakharbor-legal.com</p>
  </section>

  <section class="card card--back" aria-label="Card back">
    <div class="back-mark" role="img" aria-label="Firm silhouette logo: two standing men in suits"></div>
    <div class="contact">
      <h2 class="contact-name">Dorian Kestrup</h2>
      <p class="contact-role">Law Firm</p>
      <ul class="contact-list">
        <li class="contact-item">
          <svg class="contact-icon" viewBox="0 0 24 24" aria-hidden="true">
            <path d="M6.6 10.8a15.1 15.1 0 0 0 6.6 6.6l2.2-2.2c.3-.3.7-.4 1-.2 1.1.4 2.3.6 3.6.6.6 0 1 .4 1 1V20c0 .6-.4 1-1 1A17 17 0 0 1 3 4c0-.6.4-1 1-1h3.5c.6 0 1 .4 1 1 0 1.3.2 2.5.6 3.6.1.3 0 .7-.2 1z"/>
          </svg>
          <span>800-555-0147</span>
        </li>
        <li class="contact-item">
          <svg class="contact-icon" viewBox="0 0 24 24" aria-hidden="true">
            <path d="M1 5h22v14H1z M3 7v.4l9 6 9-6V7z M3 9.8V17h18V9.8l-9 6z" fill-rule="evenodd"/>
          </svg>
          <span>dorian@oakharbor-legal.com</span>
        </li>
        <li class="contact-item">
          <svg class="contact-icon" viewBox="0 0 24 24" aria-hidden="true">
            <circle cx="12" cy="12" r="10" fill="none" stroke="var(--back-ink)" stroke-width="2.2"/>
          </svg>
          <span>www.oakharbor-legal.com</span>
        </li>
      </ul>
    </div>
    <div class="back-band"></div>
  </section>
</body>
</html>
```